Marlowe Shopcraft Interiors web design

We need to relaunch my commercial and retail interior design + construction company after being out of the industry's for 10 plus years.

```html
<!DOCTYPE html>
<html lang="en">
<head>
<meta charset="utf-8">
<title>Marlowe Shopcraft Interiors – Web Design</title>
<link rel="stylesheet" href="https://fonts.googleapis.com/css2?family=Syncopate:wght@700&family=Barlow:wght@400;500;600&family=Barlow+Condensed:wght@400&display=swap">
<style>
:root{
  --blue:#1a8cf0;
  --ink:#1e1e1e;
  --dark:#262626;
  --board:#9d9d9d;
  --light:#f2f3f5;
  --line:#d4d6da;
  --text:#3a3a3a;
  --white:#fff;
}
*{box-sizing:border-box;margin:0;padding:0}
html,body{width:1200px;height:2776px;overflow:hidden;background:var(--board)}
.board{position:absolute;left:0;top:0;width:1113px;height:2576px;transform:scale(1.0782);transform-origin:0 0;font-family:"Barlow",sans-serif;color:var(--text)}
.abs{position:absolute}
.head{font-family:"Syncopate",sans-serif;font-weight:700;color:var(--ink);text-transform:uppercase;letter-spacing:.3px;line-height:1.25}
.blue{color:var(--blue)}
.ph{position:absolute}
.page{position:absolute;left:33px;top:25px;width:540px;height:2518px;background:var(--white);overflow:hidden}
.brand{display:flex;align-items:center;gap:5px;font-family:"Syncopate",sans-serif;font-weight:700;font-size:6px;line-height:1.2;color:var(--ink);text-transform:uppercase}
.brand .sq{width:11px;height:11px;background:var(--blue)}
.brand.light{color:#fff}
.small{font-size:6px;line-height:1.55}
.tiny{font-size:4.6px;line-height:1.55}
.card{position:absolute;background:var(--white)}
.btn{position:absolute;border:1px solid var(--blue);color:var(--blue);font-size:5.5px;font-weight:600;display:flex;align-items:center;justify-content:center}
.icon{position:absolute;width:32px;height:32px;border-radius:50%;background:var(--blue);display:flex;align-items:center;justify-content:center}
.svc{position:absolute;width:90px;border:1px solid rgba(255,255,255,.75);color:var(--white)}
.svc .shot{position:relative;width:100%;height:63px;background:linear-gradient(135deg,#e1e4e8,#9aa1a9 60%,#5e656d)}
.svc .lbl{position:absolute;top:49px;left:6px;right:4px;font-size:5.3px;font-weight:600;text-transform:uppercase;color:#fff;line-height:1.15}
.svc p{font-size:5px;line-height:1.4;padding:4px 8px 6px;min-height:38px}
.team{position:absolute;width:142px}
.team .img{height:105px}
.team .panel{position:absolute;top:82px;left:4px;width:134px;height:110px;background:#fff;border:1px solid var(--line);padding:10px 12px}
.team .panel h4{font-family:"Syncopate",sans-serif;font-weight:700;font-size:6.2px;text-transform:uppercase;color:var(--ink);line-height:1.2;margin-bottom:6px}
.team .panel p{font-size:5.4px;line-height:1.65}
.why{position:absolute;top:88px;width:104px;height:104px;border:1px solid var(--line);background:#fff;text-align:center;padding:26px 7px 0}
.why h4{font-family:"Syncopate",sans-serif;font-weight:700;font-size:5.2px;text-transform:uppercase;color:var(--ink);margin-bottom:6px}
.why p{font-size:4.8px;line-height:1.6}
.testi{position:absolute;top:66px;width:190px;height:109px;background:#fff;border:1px solid var(--line);text-align:center;padding:28px 22px 0}
.testi b{display:block;font-size:6px;color:var(--ink);line-height:1.5;margin-bottom:3px}
.testi p{font-size:5.4px;line-height:1.6}
.testi .who{font-family:"Syncopate",sans-serif;font-weight:700;font-size:4.6px;color:var(--ink);margin-top:10px}
.avatar{position:absolute;top:46px;width:30px;height:30px;border-radius:50%;background:linear-gradient(#c9c2bb,#8a7f76);border:2px solid #fff}
.field{position:absolute;left:25px;width:170px;height:19px;border:1px solid var(--line);font-size:5px;padding:5px 8px;color:#555}
.contact-col{position:absolute;top:80px;width:150px;text-align:center}
.contact-col .lab{font-size:6.5px;color:#555;letter-spacing:.3px;margin-top:8px}
.contact-col .val{font-size:7.5px;font-weight:500;color:var(--ink);line-height:1.25}
.banner{position:absolute;left:606px;width:479px;overflow:hidden}
.banner .hl{font-family:"Syncopate",sans-serif;font-weight:700;text-transform:uppercase;color:var(--ink)}
</style>
</head>
<body>
<div class="board">

  <!-- ================= WEBSITE PAGE ================= -->
  <div class="page">

    <!-- header -->
    <div class="abs brand" style="left:57px;top:5px"><span class="sq"></span><span>Marlowe<br>Shopcraft<br>Interiors</span></div>
    <div class="abs head" style="left:302px;top:13px;font-size:5px;font-family:'Barlow',sans-serif;font-weight:500;letter-spacing:.4px">Welcome to <b>Marlowe Shopcraft Interiors</b></div>

    <!-- hero -->
    <div class="ph" role="img" aria-label="Bright modern open-plan office interior with stairs and large windows" style="left:0;top:35px;width:540px;height:266px;background:linear-gradient(180deg,#eef0f2 0%,#d7d9dc 55%,#a9a39c 100%)"></div>
    <div class="abs head" style="left:107px;top:101px;width:325px;height:56px;border:2px solid var(--blue);font-size:11.5px;text-align:center;padding-top:8px;line-height:1.5">Have you experienced<br><span class="blue">frustration</span> in the design and<br>building process?</div>
    <svg class="abs" style="left:258px;top:290px" width="22" height="22" viewBox="0 0 22 22"><rect x="4" y="4" width="14" height="14" transform="rotate(45 11 11)" fill="#fff"/><path d="M11 6v9M8 12l3 3 3-3" stroke="var(--blue)" fill="none" stroke-width="1.2"/></svg>

    <!-- intro -->
    <div class="ph" role="img" aria-label="Reception area with timber wall panelling and lounge chairs" style="left:53px;top:343px;width:245px;height:175px;background:linear-gradient(135deg,#d8d8d6,#a89680 55%,#8d8c8a)"></div>
    <div class="abs" style="left:445px;top:350px;width:57px;height:153px;border:6px solid var(--blue);border-left:none"></div>
    <div class="card" style="left:272px;top:358px;width:223px;height:139px;padding:22px 17px 0 18px;box-shadow:0 2px 6px rgba(0,0,0,.08)">
      <p style="font-size:7.3px;color:var(--ink);line-height:1.35;margin-bottom:6px">Are you in search of a fresh approach to guarantee superior outcomes for your upcoming commercial and retail interior fitouts?</p>
      <p class="small" style="font-size:5.8px">At Marlowe Shopcraft Interiors, we were founded with your needs at the forefront—a dedication to delivering a transformative leap in results for your commercial and retail projects. Our pride lies in surpassing client expectations, achieved through meticulous planning and proactive problem-solving before challenges even surface.</p>
    </div>

    <!-- dark band -->
    <div class="abs" style="left:0;top:546px;width:540px;height:93px;background:var(--dark);color:#e6e6e6;font-size:6.8px;line-height:1.55;text-align:center;padding:17px 72px 0">Guided by the expertise of interior designer and commercial builder, Mr. Daniel Hartwell since 1994, our dedicated team seamlessly manages every facet of your project. From meticulous planning and innovative design to thorough documentation, efficient project management, expert construction, and thorough maintenance, we bring precision, purpose, value, and passion to every stage. Our commitment ensures that your high-end commercial and retail fitouts are not just met but exceeded—delivering on time, on budget, and hassle-free.”</div>

    <!-- photo strip -->
    <div class="ph" role="img" aria-label="Retail store frontage with fashion mannequins" style="left:0;top:639px;width:136px;height:106px;background:linear-gradient(135deg,#b44fa0,#4a4d7a 60%,#c9c9d4)"></div>
    <div class="ph" role="img" aria-label="Boutique interior with fashion display" style="left:137px;top:639px;width:136px;height:106px;background:linear-gradient(135deg,#3a3537,#c3b9b1 55%,#d277b9)"></div>
    <div class="ph" role="img" aria-label="Jewellery store fitout with glass cabinets" style="left:274px;top:639px;width:136px;height:106px;background:linear-gradient(135deg,#5b4a36,#c2a772 55%,#2f2a22)"></div>
    <div class="ph" role="img" aria-label="Minimal fashion retail interior" style="left:411px;top:639px;width:129px;height:106px;background:linear-gradient(135deg,#e6e3df,#b7aea5 60%,#6e6560)"></div>

    <!-- why choose -->
    <div class="ph" role="img" aria-label="Faint architectural sketch background" style="left:0;top:745px;width:540px;height:227px;background:linear-gradient(180deg,#f3f4f6,#e9ebee)"></div>
    <div class="abs head" style="left:0;top:770px;width:540px;text-align:center;font-size:9.5px">Why choose Marlowe<br><span class="blue">Shopcraft Interiors?</span></div>
    <div class="abs" style="left:0;top:745px;width:540px;height:227px">
      <div class="why" style="left:56px"><h4>Holistic<br>Approach</h4><p>From concept to completion, we deliver client-focused results, providing a holistic, compliant, and innovative business</p></div>
      <div class="why" style="left:166px"><h4>Specialisations</h4><p>We specialise in a range of projects, including Medicinal Cannabis dispensaries, Medical centers, Pharmacy and health food outlets, Strongroom safe supply and installation, Offices, retail, hospitality, and showrooms.</p></div>
      <div class="why" style="left:276px"><h4>Peace of mind</h4><p>Our customers enjoy peace of mind, security, safety, and compliance throughout the design and construction phases.</p></div>
      <div class="why" style="left:386px"><h4>Compliance</h4><p>Registered with the State Building Board as commercial builder and interior designer.</p></div>
      <div class="icon" style="left:91px;top:73px"><svg width="16" height="16" viewBox="0 0 16 16" fill="none" stroke="#fff" stroke-width="1.1"><circle cx="8" cy="5" r="3"/><path d="M3 14c0-3 2.2-5 5-5s5 2 5 5"/></svg></div>
      <div class="icon" style="left:201px;top:73px"><svg width="16" height="16" viewBox="0 0 16 16" fill="none" stroke="#fff" stroke-width="1.1"><rect x="3" y="2" width="10" height="12"/><path d="M6 5h4M6 8h4M6 11h4"/></svg></div>
      <div class="icon" style="left:311px;top:73px"><svg width="16" height="16" viewBox="0 0 16 16" fill="none" stroke="#fff" stroke-width="1.1"><circle cx="8" cy="7" r="5"/><path d="M6 7l1.5 1.5L11 5"/></svg></div>
      <div class="icon" style="left:421px;top:73px"><svg width="16" height="16" viewBox="0 0 16 16" fill="none" stroke="#fff" stroke-width="1.1"><rect x="3" y="3" width="10" height="10"/><path d="M5.5 8l2 2 3.5-4"/></svg></div>
    </div>

    <!-- teams -->
    <div class="abs head" style="left:54px;top:993px;font-size:10px">Our expert <span class="blue">teams</span></div>
    <div class="abs" style="left:54px;top:1009px;width:16px;height:1.5px;background:var(--ink)"></div>
    <div class="team" style="left:53px;top:1028px">
      <div class="ph img" role="img" aria-label="Consulting team meeting around a table" style="width:142px;background:linear-gradient(135deg,#8a7a6a,#d9cfc2 60%,#4b4a48)"></div>
      <div class="abs" style="left:4px;top:100px;width:134px;height:95px;border-left:4px solid var(--blue);border-bottom:4px solid var(--blue)"></div>
      <div class="panel"><h4>Consulting<br><span class="blue">Team</span></h4><p>Our consulting team comprises project managers, interior designers, architects, town planners, acoustic, structural, mechanical, fire services engineers, building surveyors, and DDA consultants, ensuring compliant and innovative design and construction solutions.</p></div>
    </div>
    <div class="team" style="left:207px;top:1028px">
      <div class="ph img" role="img" aria-label="Construction workers in hard hats on site" style="width:142px;background:linear-gradient(135deg,#b9b7b2,#c98a3c 55%,#5a6270)"></div>
      <div class="abs" style="left:4px;top:100px;width:134px;height:95px;border-left:3px solid #aaa;border-bottom:3px solid #aaa;border-right:3px solid #aaa"></div>
      <div class="panel"><h4>Consulting<br><span class="blue">Team</span></h4><p>The MSI construction team consists of skilled professionals, including site supervisors, carpenters, plasterers, electricians, data and IT specialists, security experts, plumbers, flooring specialists, joiners, glazers, and painters.</p></div>
    </div>
    <div class="team" style="left:359px;top:1028px">
      <div class="ph img" role="img" aria-label="Finance consultants in business attire" style="width:142px;background:linear-gradient(135deg,#e2e2e4,#9f8b78 50%,#24272d)"></div>
      <div class="abs" style="left:4px;top:100px;width:134px;height:95px;border-left:3px solid var(--ink);border-bottom:3px solid var(--ink)"></div>
      <div class="panel"><h4>Finance and leagal<br><span class="blue">consulting</span></h4><p>Explore fitout and construction finance options with our finance consulting team, providing you with alternatives to fund your projects without tapping into your business, home loan, or superannuation.</p></div>
    </div>

    <!-- services -->
    <div class="abs" style="left:0;top:1258px;width:540px;height:317px;background:var(--blue)"></div>
    <div class="abs head" style="left:0;top:1281px;width:540px;text-align:center;font-size:9px;color:#fff">Services we offer</div>
    <div class="abs" style="left:262px;top:1297px;width:16px;height:1.5px;background:#fff"></div>
    <div class="svc" style="left:44px;top:1317px"><div class="shot" role="img" aria-label="Site inspection paperwork"></div><span class="lbl">Site Inspection</span><p>Pre-lease site inspections and advice on base building works.</p></div>
    <div class="svc" style="left:138px;top:1317px"><div class="shot" role="img" aria-label="Budget plans and drawings"></div><span class="lbl">Budgeting</span><p>Expert advice on construction budgets and required services.</p></div>
    <div class="svc" style="left:232px;top:1317px"><div class="shot" role="img" aria-label="Hard hat on planning drawings"></div><span class="lbl">Planning Services</span><p>Comprehensive planning from start to finish.</p></div>
    <div class="svc" style="left:326px;top:1317px"><div class="shot" role="img" aria-label="Consultants reviewing plans"></div><span class="lbl">Consultation</span><p>Collaborate with disability access consultants, architects, interior designers, and various engineering disciplines.</p></div>
    <div class="svc" style="left:420px;top:1317px"><div class="shot" role="img" aria-label="Approved stamp on documents"></div><span class="lbl">Design Approval</span><p>Submission and approval processes for design fitouts in shopping centers.</p></div>
    <div class="svc" style="left:92px;top:1437px"><div class="shot" role="img" aria-label="Joiners at work"></div><span class="lbl" style="top:43px">Dispensary<br>Joinery</span><p>Specialized joinery solutions for dispensaries.</p></div>
    <div class="svc" style="left:186px;top:1437px"><div class="shot" role="img" aria-label="Building under construction"></div><span class="lbl" style="top:43px">Design and<br>Construction</span><p>Seamless coordination of design and construction solutions.</p></div>
    <div class="svc" style="left:280px;top:1437px"><div class="shot" role="img" aria-label="Renovated kitchen interior"></div><span class="lbl" style="top:43px">Renovations and<br>Rebranding</span><p>Vacant and demolishing works, shop front renovations, signage updates, and removals.</p></div>
    <div class="svc" style="left:374px;top:1437px"><div class="shot" role="img" aria-label="Permit application form"></div><span class="lbl" style="top:43px">Permit<br>Applications</span><p>Assistance in obtaining building, health, and town planning permits.</p></div>

    <!-- call to action -->
    <div class="ph" role="img" aria-label="Modern open-plan office with white desks and planters" style="left:241px;top:1606px;width:239px;height:174px;background:linear-gradient(135deg,#e5e7ea,#b7bcc2 55%,#4f5a4c)"></div>
    <div class="abs" style="left:49px;top:1615px;width:60px;height:151px;border:6px solid var(--blue);border-right:none"></div>
    <div class="card" style="left:57px;top:1621px;width:224px;height:139px;padding:23px 17px 0;box-shadow:0 2px 6px rgba(0,0,0,.08)">
      <p style="font-size:7.4px;color:var(--ink);line-height:1.35;margin-bottom:9px">If you're searching for a superior way to design and construct your next project, contact us to arrange an obligation-free consultation.</p>
      <p style="font-size:7.4px;color:var(--ink);line-height:1.35">Experience the Marlowe Shopcraft Interiors difference—where excellence meets innovation!</p>
      <div class="btn" style="left:17px;top:103px;width:72px;height:19px">CONTACT US</div>
    </div>

    <!-- testimonials -->
    <div class="ph" role="img" aria-label="Faint architectural sketch background" style="left:0;top:1810px;width:540px;height:233px;background:linear-gradient(180deg,#f1f2f4,#e6e8eb)"></div>
    <div class="abs" style="left:0;top:1810px;width:540px;height:233px">
      <div class="abs head" style="left:0;top:26px;width:540px;text-align:center;font-size:9.5px">Testimonials</div>
      <div class="abs" style="left:262px;top:42px;width:16px;height:1.5px;background:var(--ink)"></div>
      <div class="testi" style="left:72px"><b>Lorem ipsum dolor sit amet, consectetur adipiscing elit sed do eiusmod</b><p>incididunt ut labore et dolore magna aliqua. Ut enim ad minim veniam, quis nostrud exercitation ullamco laboris nisi ut aliquip ex ea commod</p><div class="who">AARON WHITFIELD</div></div>
      <div class="testi" style="left:280px"><b>Lorem ipsum dolor sit amet, consectetur adipiscing elit sed do eiusmod</b><p>incididunt ut labore et dolore magna aliqua. Ut enim ad minim veniam, quis nostrud exercitation ullamco laboris nisi ut aliquip ex ea commod</p><div class="who">AARON WHITFIELD</div></div>
      <div class="avatar" role="img" aria-label="Client portrait" style="left:152px"></div>
      <div class="avatar" role="img" aria-label="Client portrait" style="left:358px"></div>
      <div class="abs" style="left:239px;top:206px;width:19px;height:2px;background:var(--ink)"></div>
      <div class="abs" style="left:266px;top:206px;width:19px;height:2px;background:#c9cbcf"></div>
      <div class="abs" style="left:293px;top:206px;width:19px;height:2px;background:#c9cbcf"></div>
    </div>

    <!-- contact -->
    <div class="abs" style="left:0;top:2043px;width:540px;height:400px">
      <div class="abs" style="left:0;top:27px;width:540px;text-align:center;font-size:7px;letter-spacing:.5px;color:#555">GET IN TOUCH</div>
      <div class="abs head" style="left:0;top:38px;width:540px;text-align:center;font-size:10.5px">Contact us</div>
      <div class="abs" style="left:262px;top:56px;width:16px;height:1.5px;background:var(--ink)"></div>
      <div class="contact-col" style="left:55px">
        <svg width="20" height="20" viewBox="0 0 20 20"><circle cx="10" cy="10" r="10" fill="var(--blue)"/><path d="M10 4.5a3.6 3.6 0 0 0-3.6 3.6c0 2.8 3.6 7 3.6 7s3.6-4.2 3.6-7A3.6 3.6 0 0 0 10 4.5z" fill="#fff"/><circle cx="10" cy="8.1" r="1.3" fill="var(--blue)"/></svg>
        <div class="lab">LOCATION</div><div class="val">Level 4, 118 Carrow Lane,<br>Southbank VIC 3006</div>
      </div>
      <div class="abs" style="left:204px;top:83px;width:1px;height:46px;background:var(--line)"></div>
      <div class="contact-col" style="left:203px">
        <svg width="20" height="20" viewBox="0 0 20 20"><circle cx="10" cy="10" r="10" fill="var(--blue)"/><path d="M7 5l2 2.5-1.2 1.3c.7 1.5 1.9 2.7 3.4 3.4l1.3-1.2L15 13l-1.2 1.8C9.5 14.5 5.5 10.5 5.2 6.2z" fill="#fff"/></svg>
        <div class="lab">PHONE NUMBER</div><div class="val" style="font-weight:600">0800 555 014</div>
      </div>
      <div class="abs" style="left:337px;top:83px;width:1px;height:46px;background:var(--line)"></div>
      <div class="contact-col" style="left:337px">
        <svg width="20" height="20" viewBox="0 0 20 20"><circle cx="10" cy="10" r="10" fill="var(--blue)"/><rect x="5" y="6.5" width="10" height="7" fill="#fff"/><path d="M5 6.5l5 4 5-4" stroke="var(--blue)" fill="none" stroke-width=".9"/></svg>
        <div class="lab">EMAIL US</div><div class="val">hello@marloweshopcraft.example</div>
      </div>

      <div class="ph" role="img" aria-label="Street map showing the office location" style="left:52px;top:162px;width:232px;height:198px;background:linear-gradient(135deg,#f4f4f4,#e1e1e1)"></div>
      <div class="card" style="left:136px;top:272px;width:97px;height:34px;border:1px solid #bbb;font-size:5.3px;text-align:center;padding-top:9px;line-height:1.4;color:var(--ink)">Level 4, 118 Carrow Lane,<br>Southbank VIC 3006</div>
      <div class="abs" style="left:451px;top:313px;width:50px;height:53px;background:var(--blue)"></div>
      <div class="card" style="left:282px;top:162px;width:213px;height:198px;box-shadow:0 2px 6px rgba(0,0,0,.08)">
        <div class="abs head" style="left:25px;top:24px;font-size:7.5px;line-height:1.35"><span class="blue">Book a free</span><br>consultation here</div>
        <div class="abs" style="left:25px;top:51px;font-size:5.6px;color:#444">Stage in Touch with us or enquire.</div>
        <div class="field" style="top:68px">Name</div>
        <div class="field" style="top:93px">Email address</div>
        <div class="field" style="top:118px;height:37px">Message</div>
        <div class="abs" style="left:25px;top:162px;width:172px;height:19px;background:var(--blue);color:#fff;font-size:5.5px;font-weight:600;display:flex;align-items:center;justify-content:center">SEND MESSAGE</div>
      </div>
    </div>

    <!-- footer -->
    <div class="abs brand" style="left:77px;top:2422px;font-size:7.5px"><span class="sq" style="width:14px;height:14px"></span><span>Marlowe<br>Shopcraft<br>Interiors</span></div>
    <div class="abs" role="img" aria-label="Registered practitioner badge" style="left:225px;top:2420px;width:30px;height:30px;border-radius:50%;background:#8b93a3"></div>
    <div class="abs" role="img" aria-label="Building regulator badge" style="left:383px;top:2420px;width:68px;height:30px;background:#1f4f9a"></div>
    <div class="abs" style="left:0;top:2495px;width:540px;text-align:center;font-size:6.3px;color:#444">Copyright © 2024 Marlowe Shopcraft Interiors Pty Ltd</div>
  </div>

  <!-- ================= BANNER VARIATIONS ================= -->
  <div class="abs" style="left:606px;top:18px;width:479px;text-align:center;font-family:'Barlow Condensed',sans-serif;font-size:31px;color:#111;letter-spacing:.5px">TOP BANNER VARIATIONS</div>

  <!-- banner 1 -->
  <div class="banner" style="top:70px;height:254px;background:#fff">
    <div class="ph" role="img" aria-label="Architectural pencil sketch of an office interior" style="left:220px;top:0;width:259px;height:254px;background:linear-gradient(90deg,rgba(255,255,255,1),#d8dadd 40%,#9fa3a8)"></div>
    <div class="abs brand" style="left:44px;top:15px"><span class="sq"></span><span>Marlowe<br>Shopcraft<br>Interiors</span></div>
    <div class="abs" style="left:44px;top:68px;font-size:5px;text-transform:uppercase;color:var(--ink);letter-spacing:.3px">Welcome to <b>Marlowe Shopcraft Interiors</b></div>
    <div class="abs hl" style="left:44px;top:80px;font-size:11.5px;line-height:1.2">Have you<br>experienced<br><span class="blue">frustration</span> in the<br>design and building<br>process?</div>
    <p class="abs tiny" style="left:44px;top:160px;width:195px;font-size:5px">Are you in search of a fresh approach to guarantee superior outcomes for your upcoming commercial and retail interior fitouts? At Marlowe Shopcraft Interiors, we were founded with your needs at the forefront—a dedication to delivering a transformative leap in results for your commercial and retail projects. Our pride lies in surpassing client expectations, achieved through meticulous planning and proactive problem-solving before challenges even surface</p>
  </div>

  <!-- banner 2 -->
  <div class="banner" style="top:352px;height:248px;background:#1f1f1f">
    <div class="ph" role="img" aria-label="Open-plan office with black desk chairs" style="left:230px;top:0;width:249px;height:248px;background:linear-gradient(90deg,#2a2a2a,#c9ccd0 35%,#f0f1f2 70%,#8a8d91)"></div>
    <div class="abs brand light" style="left:46px;top:8px"><span class="sq"></span><span>Marlowe<br>Shopcraft<br>Interiors</span></div>
    <div class="abs" style="left:242px;top:12px;font-size:5px;color:#fff;text-transform:uppercase;letter-spacing:.3px">Welcome to <b>Marlowe Shopcraft Interiors</b></div>
    <div class="abs hl" style="left:44px;top:80px;font-size:8.5px;line-height:1.65;color:#fff">Have you experienced<br>frustration in the design<br>and building process?</div>
    <p class="abs tiny" style="left:46px;top:128px;width:195px;font-size:5px;color:#ddd">Are you in search of a fresh approach to guarantee superior outcomes for your upcoming commercial and retail interior fitouts? At Marlowe Shopcraft Interiors, we were founded with your needs at the forefront—a dedication to delivering a transformative leap in results for your commercial and retail projects. Our pride lies in surpassing client expectations, achieved through meticulous planning and proactive problem-solving before challenges even surface</p>
  </div>

  <!-- banner 3 -->
  <div class="banner" style="top:634px;height:250px;background:#fff">
    <div class="ph" role="img" aria-label="Sketch blending into a photographed office interior" style="left:0;top:130px;width:479px;height:120px;background:linear-gradient(90deg,#f0f0f0,#dadde0 50%,#c2c6ca)"></div>
    <div class="ph" role="img" aria-label="Bright office with workstations and city views" style="left:250px;top:0;width:229px;height:250px;background:linear-gradient(135deg,#eef0f2,#c3c8cd 60%,#9aa0a6)"></div>
    <div class="abs brand" style="left:52px;top:12px"><span class="sq"></span><span>Marlowe<br>Shopcraft<br>Interiors</span></div>
    <div class="abs" style="left:264px;top:18px;font-size:5px;line-height:1.5;text-transform:uppercase;color:var(--ink);letter-spacing:.3px">Welcome to<br>Marlowe Shopcraft Interiors</div>
    <div class="abs hl" style="left:52px;top:62px;font-size:7px;line-height:1.35">Have you experienced<br><span class="blue">frustration</span> in the<br>design and building process?</div>
    <p class="abs tiny" style="left:52px;top:98px;width:183px;font-size:4.6px;background:rgba(255,255,255,.85)">Are you in search of a fresh approach to guarantee superior outcomes for your upcoming commercial and retail interior fitouts? At Marlowe Shopcraft Interiors, we were founded with your needs at the forefront—a dedication to delivering a transformative leap in results for your commercial and retail projects. Our pride lies in surpassing client expectations, achieved through meticulous planning and proactive problem-solving before challenges even surface</p>
  </div>

  <!-- banner 4 -->
  <div class="banner" style="top:928px;height:284px">
    <svg class="abs" style="left:0;top:0" width="479" height="284" viewBox="0 0 479 284">
      <defs><linearGradient id="room" x1="0" y1="0" x2="0" y2="1"><stop offset="0" stop-color="#e9ebed"/><stop offset=".5" stop-color="#f7f7f8"/><stop offset="1" stop-color="#c8cacd"/></linearGradient></defs>
      <path d="M0 0H479V218L240 280L0 218Z" fill="url(#room)" role="img" aria-label="Empty white commercial space"/>
      <path d="M0 218L240 280L479 218" fill="none" stroke="var(--blue)" stroke-width="3"/>
    </svg>
    <div class="abs brand" style="left:46px;top:7px"><span class="sq"></span><span>Marlowe<br>Shopcraft<br>Interiors</span></div>
    <div class="abs" style="left:262px;top:10px;font-size:5px;text-transform:uppercase;color:var(--ink);letter-spacing:.3px">Welcome to <b>Marlowe Shopcraft Interiors</b></div>
    <div class="abs" style="left:105px;top:78px;width:279px;height:44px;border:2px solid var(--blue);border-top:none"></div>
    <div class="abs" style="left:105px;top:78px;width:40px;height:2px;background:var(--blue)"></div>
    <div class="abs" style="left:342px;top:78px;width:42px;height:2px;background:var(--blue)"></div>
    <div class="abs hl" style="left:105px;top:72px;width:279px;text-align:center;font-size:9px;line-height:1.6">Have you experienced<br><span class="blue">frustration</span> in the design and<br>building process?</div>
    <p class="abs" style="left:100px;top:132px;width:280px;text-align:center;font-size:7px;line-height:1.3;color:var(--ink)">Are you in search of a fresh approach to guarantee superior outcomes for your upcoming commercial and retail interior fitouts?</p>
    <p class="abs tiny" style="left:100px;top:154px;width:280px;text-align:center;font-size:4.8px">At Marlowe Shopcraft Interiors, we were founded with your needs at the forefront—a dedication to delivering a transformative leap in results for your commercial and retail projects. Our pride lies in surpassing client expectations, achieved through meticulous planning and proactive problem-solving before challenges even surface</p>
  </div>

</div>
</body>
</html>
```